Web-Design for Electrcian Company

Our Customer is a small business electrian in Switzerland. He is looking for a fresh and innovative website design. He is well known for his extra service, and that they always go for the extra-mile! In his logo you also see that positive and fresh image the try to bring to the customer. the main colors are black, red and white.

the website structure will be:

- home
- services (with submenu for each service)
- references (with submenu for each category of services)
- about us (2 submenus: history and staff)
- links
- Contact

Target Market(s)

Architects, building owners, people from the age of 35 up...

Industry/Entity Type

Small Business

```html
<!DOCTYPE html>
<html lang="en">
<head>
<meta charset="utf-8">
<title>Brunner + Vogel Elektro AG</title>
<link href="https://fonts.googleapis.com/css2?family=Source+Sans+3:ital,wght@0,400;0,600;0,700;1,800;1,900&display=swap" rel="stylesheet">
<style>
:root{
  --red:#c8141e;
  --red-dark:#8c0a10;
  --red-deep:#6e0509;
  --red-bright:#e0222c;
  --white:#ffffff;
  --ink:#1a1a1a;
  --grey-text:#4a4a4a;
  --btn-top:#f4f4f5;
  --btn-bottom:#c9cacd;
  --gold:#f2b312;
}
*{margin:0;padding:0;box-sizing:border-box}
html,body{width:1200px;height:675px;overflow:hidden;background:var(--white);font-family:"Source Sans 3",Arial,sans-serif}
.page{position:absolute;left:161px;top:0;width:878px;height:675px;overflow:hidden;
  background:
    radial-gradient(ellipse 60% 30% at 20% 70%,rgba(255,90,90,.35),transparent 70%),
    radial-gradient(ellipse 70% 25% at 85% 55%,rgba(230,20,30,.5),transparent 70%),
    linear-gradient(170deg,var(--red-dark) 0%,var(--red) 45%,var(--red-deep) 70%,var(--red) 100%);}
.brand-band{position:absolute;left:0;top:53px;width:249px;height:70px;background:var(--white);display:flex;align-items:center;padding-left:8px}
.brand-name{font-size:19px;font-weight:600;color:var(--ink);letter-spacing:-.2px;white-space:nowrap}
.brand-mark{position:absolute;left:249px;top:40px;width:106px;height:94px;background:var(--white);border-radius:6px;display:flex;align-items:center;justify-content:center}
.brand-mark span{width:70px;height:70px;border:4px solid var(--red);border-radius:50%}
.helpline{position:absolute;left:660px;top:82px;display:flex;align-items:center;gap:6px;color:var(--white)}
.helpline-label{font-size:12px;line-height:1}
.helpline-number{font-size:21px;font-weight:600;line-height:1}
.nav{position:absolute;left:52px;top:149px;width:196px;height:280px;background:rgba(255,255,255,.12);border-radius:6px;padding:11px 12px}
.nav a{display:block;text-decoration:none}
.nav-item{height:33px;margin-bottom:1px;border-radius:3px;background:linear-gradient(var(--btn-top),var(--btn-bottom));color:var(--ink);font-size:16px;line-height:33px;padding-left:18px}
.nav-item.is-active{background:linear-gradient(var(--red-bright),#a90f17);color:var(--white)}
.subnav{list-style:none;padding:8px 0 9px 18px}
.subnav li{color:var(--white);font-size:13px;line-height:21px;padding-left:13px;position:relative}
.subnav li::before{content:"";position:absolute;left:0;top:8px;border-left:4px solid var(--white);border-top:3px solid transparent;border-bottom:3px solid transparent}
.content{position:absolute;left:249px;top:149px;width:578px;height:411px;background:var(--white);border-radius:3px}
.hero{position:absolute;left:9px;top:9px;width:561px;height:264px;border-radius:5px;overflow:hidden;
  background:linear-gradient(115deg,#3a3a40 0%,#7d5a2c 25%,#c99a55 45%,#2f5aa8 75%,#c98c5a 100%)}
.hero-title{position:absolute;left:38px;top:142px;font-style:italic;font-weight:900;line-height:1;text-transform:uppercase}
.hero-title .l1{display:block;color:var(--white);font-size:36px;padding-left:40px}
.hero-title .l2{display:block;color:var(--gold);font-size:42px}
.hero-title .l3{display:block;color:var(--white);font-size:24px;padding-left:75px}
.dots{position:absolute;right:18px;bottom:10px;display:flex;gap:6px}
.dots i{width:8px;height:8px;border-radius:50%;background:var(--white)}
.dots i.is-current{background:var(--red)}
.teaser{position:absolute;top:284px;width:190px;height:120px}
.teaser h2{font-size:19px;font-weight:400;color:var(--red);margin-bottom:8px}
.teaser p{font-size:10.5px;line-height:10.5px;color:var(--grey-text);text-align:justify}
.teaser .link{display:block;font-size:10.5px;color:var(--grey-text);text-decoration:underline;margin-top:5px}
.btn{position:absolute;bottom:0;width:65px;height:21px;background:var(--red);color:var(--white);font-size:11px;line-height:21px;text-align:center;border-radius:2px;text-decoration:none}
.teaser-news{left:16px}
.teaser-news p{padding-left:3px;width:150px}
.teaser-team{left:216px;border-left:1px solid #eee;box-shadow:-8px 0 8px -8px rgba(0,0,0,.25)}
.teaser-team h2,.teaser-team .faces{margin-left:11px}
.teaser-team .btn{left:11px}
.faces{display:flex;gap:2px}
.face{width:48px;height:52px;border:1px solid #ccc;background:linear-gradient(#d8d2cc,#9c8c80)}
.teaser-services{left:412px;border-left:1px solid #eee;box-shadow:-8px 0 8px -8px rgba(0,0,0,.25);padding-left:11px}
.teaser-services .btn{left:11px}
.teaser-services p{width:150px}
.footer{position:absolute;left:53px;top:574px;width:774px;height:57px;background:var(--white);border-radius:5px 5px 0 0;padding:16px 28px}
.footer-links{font-size:10px;color:var(--red)}
.footer-links a{color:var(--red);text-decoration:none}
.footer-links .sep{margin:0 4px}
.copyright{font-size:10px;color:var(--red);margin-top:2px}
.social{position:absolute;right:29px;top:15px;display:flex;gap:4px}
.social i{width:26px;height:26px;border-radius:50%;background:var(--red)}
.footer-fade{position:absolute;left:53px;top:631px;width:774px;height:28px;background:linear-gradient(rgba(255,255,255,.25),transparent)}
</style>
</head>
<body>
<div class="page">
  <div class="brand-band"><span class="brand-name">Brunner + Vogel Elektro AG</span></div>
  <div class="brand-mark"><span></span></div>

  <div class="helpline">
    <svg width="24" height="50" viewBox="0 0 24 50" aria-hidden="true"><path d="M16 2 L22 4 L17 16 L12 15 C8 22 8 30 12 36 L17 34 L22 45 L16 48 C2 38 2 12 16 2 Z" fill="#fff"/></svg>
    <div><div class="helpline-label">24 Hours Help Line:</div><div class="helpline-number">1800 555 0199</div></div>
  </div>

  <nav class="nav">
    <a class="nav-item" href="#">Home</a>
    <a class="nav-item" href="#">Services</a>
    <a class="nav-item" href="#">References</a>
    <a class="nav-item is-active" href="#">About Us</a>
    <ul class="subnav"><li>History</li><li>Staff</li></ul>
    <a class="nav-item" href="#">Links</a>
    <a class="nav-item" href="#">Contact Us</a>
  </nav>

  <main class="content">
    <div class="hero" role="img" aria-label="Photo of an electrician in safety glasses stripping a wire at a cable cabinet">
      <div class="hero-title"><span class="l1">Lore</span><span class="l2">Commod</span><span class="l3">Ae Massaa</span></div>
      <div class="dots"><i></i><i class="is-current"></i><i></i><i></i></div>
    </div>

    <section class="teaser teaser-news">
      <h2>Latest News</h2>
      <p>Lorem ipsum dolor consectetuer adipiscing elit. Aenean commodo ligula eget dolor. Aenean massa. Cum sociis natoque penatibus et magnis dis parturient.</p>
      <a class="btn" href="#">View More</a>
    </section>

    <section class="teaser teaser-team">
      <h2>Our Teams</h2>
      <div class="faces">
        <div class="face" role="img" aria-label="Portrait of a team member"></div>
        <div class="face" role="img" aria-label="Portrait of a team member"></div>
        <div class="face" role="img" aria-label="Portrait of a team member"></div>
      </div>
      <a class="btn" href="#">View More</a>
    </section>

    <section class="teaser teaser-services">
      <h2>Our Services</h2>
      <p>Lorem ipsum dolor consectetuer adipiscing elit.</p>
      <a class="link" href="#">Aenean commodo ligula.</a>
      <a class="link" href="#" style="margin-top:3px">Aenean massa cum sociis.</a>
      <a class="btn" href="#">View More</a>
    </section>
  </main>

  <footer class="footer">
    <div class="footer-links"><a href="#">Home</a><span class="sep">|</span><a href="#">About Us</a><span class="sep">|</span><a href="#">Careers</a><span class="sep">|</span><a href="#">Terms &amp; Conditions</a><span class="sep">|</span><a href="#">Contact</a></div>
    <div class="copyright">Copyright © 2012. All Rights Reserved.</div>
    <div class="social"><i></i><i></i><i></i><i></i></div>
  </footer>
  <div class="footer-fade"></div>
</div>
</body>
</html>
```